Harlow Crest Holdings (Remodeling company) needs a logo and business card

We need a business card design for a new company. We "flip" upmarket houses (buy, remodel and sell) in the Austin, TX area. I'd like neutral colors (grey, white, gold black). I would like it to include a simple, clean logo. Our designs are modern and uncluttered and I would like that reflected in the business card design.

Target Market(s)

Young professionals, Families, Retirees. Our properties will sell for $750k+

Industry/Entity Type

Real Estate

Contact Information for Business Card

Harlow Crets Holdings
Mona Harlow
(979) 555 0142
Owner
Rolf Tandem
(512) 555 0176
Realtor

Logo Text

Harlow Crest Holdings

Font styles to use
Serif
Script

Requirements
Must have
• Simple, classic design
Nice to have
• Clean lines, modern look
Should not have
• Too traditionally

```html
<!DOCTYPE html>
<html lang="en">
<head>
<meta charset="utf-8">
<title>Harlow Crest Holdings – Business Cards</title>
<link href="https://fonts.googleapis.com/css2?family=Cinzel:wght@400;500&family=Josefin+Sans:wght@300&display=swap" rel="stylesheet">
<style>
  :root {
    --backdrop: #d9d6d3;
    --card: #030303;
    --gold: #c9962e;
    --gold-deep: #8a5a1c;
    --text-light: #d8d8d8;
    --text-muted: #a9a9a9;
  }
  html, body {
    margin: 0;
    padding: 0;
    width: 1200px;
    height: 1000px;
    overflow: hidden;
    background: var(--backdrop);
  }
  .canvas {
    position: relative;
    width: 1200px;
    height: 1000px;
  }
  .business-card {
    position: absolute;
    width: 580px;
    height: 332px;
    background: var(--card);
    box-shadow: 4px 6px 10px rgba(0,0,0,0.35);
  }
  .business-card--owner { left: 185px; top: 160px; }
  .business-card--realtor { left: 435px; top: 508px; }
  .card-frame {
    position: absolute;
    left: 22px; top: 22px; right: 22px; bottom: 22px;
    border: 2px solid var(--gold-deep);
    border-left-color: var(--gold);
    border-right-color: var(--gold);
  }
  .card-divider {
    position: absolute;
    left: 288px;
    top: 65px;
    width: 1px;
    height: 203px;
    background: linear-gradient(to bottom, var(--gold-deep), var(--gold), var(--gold-deep));
  }
  .brand-name {
    position: absolute;
    left: 40px;
    width: 228px;
    top: 128px;
    text-align: center;
    font-family: "Cinzel", serif;
    font-weight: 500;
    font-size: 21px;
    line-height: 26px;
    color: var(--gold);
    letter-spacing: 0.5px;
  }
  .person {
    position: absolute;
    left: 329px;
    top: 110px;
  }
  .person-name {
    font-family: "Cinzel", serif;
    font-weight: 400;
    font-size: 21px;
    color: var(--text-light);
    letter-spacing: 0.5px;
    margin: 0;
    line-height: 26px;
  }
  .person-role {
    font-family: "Cinzel", serif;
    font-size: 12px;
    color: var(--text-muted);
    margin: 4px 0 0;
    letter-spacing: 0.5px;
  }
  .contact-list {
    list-style: none;
    padding: 0;
    margin: 20px 0 0;
    font-family: "Josefin Sans", sans-serif;
    font-weight: 300;
    font-size: 11.5px;
    line-height: 16px;
    color: var(--text-muted);
  }
</style>
</head>
<body>
<main class="canvas">
  <article class="business-card business-card--owner">
    <div class="card-frame"></div>
    <div class="brand-name">Harlow Crest<br>Holdings</div>
    <div class="card-divider"></div>
    <div class="person">
      <h2 class="person-name">MONA HARLOW</h2>
      <p class="person-role">OWNER</p>
      <ul class="contact-list">
        <li>P : (979) 555 0142</li>
        <li>E : name@yourdomain.com</li>
        <li>W : yourdomain.com</li>
      </ul>
    </div>
  </article>

  <article class="business-card business-card--realtor">
    <div class="card-frame"></div>
    <div class="brand-name">Harlow Crest<br>Holdings</div>
    <div class="card-divider"></div>
    <div class="person">
      <h2 class="person-name">ROLF TANDEM</h2>
      <p class="person-role">REALTOR</p>
      <ul class="contact-list">
        <li>P : (512) 555 0176</li>
        <li>E : name@yourdomain.com</li>
        <li>W : yourdomain.com</li>
      </ul>
    </div>
  </article>
</main>
</body>
</html>
```